Web design concept for a IT recruitment agency.

Our website addresses two different target groups:
- Customers (companies) wanting to hire new IT talent
- It talent to find a new JOB

We a looking for a visual design concept that either addresses both target groups in one of the following options:
a. target both groups in 1 single splash page.
b. target both groups in 2 different pages one for both groups
c. or any creative third concept you can come up with

Requirements, we want one overall visual concept, that both target groups can relate to.

Trigger words what we want to express:
- passion / drive
- knowhow
- involvement
- professional/yet playful
- engagement

Background, company culture:
We are a recruitment agency with over 15 years of experience, we have no hard-sale culture.
But we emphasize on long term relationships, showing real interest in people and their needs.

Design requirements:
Use logo
Flat contemporary design

Target Market(s)

Industry/Entity Type

Hire

Number of Pages Required

2 page

Requirements
Must have
• We a looking for a visual design concept that either addresses both target groups

```html
<!DOCTYPE html>
<html lang="en">
<head>
<meta charset="utf-8">
<title>Norvik Staffing – IT Recruitment</title>
<link href="https://fonts.googleapis.com/css2?family=Dosis:wght@400;500;600&family=Cabin:wght@400;500&display=swap" rel="stylesheet">
<style>
  :root {
    --orange: #f15a22;
    --blue: #1e9fd8;
    --page: #f0f1f0;
    --ink: #2b2b2b;
    --muted: #6d6d6d;
    --field: rgba(14, 18, 24, 0.84);
    --field-text: #c9ccd0;
    --label-dark: rgba(22, 24, 28, 0.9);
    --rule: #c4c6c7;
    --map: #a9d3e6;
  }
  * { box-sizing: border-box; margin: 0; padding: 0; }
  html, body { width: 1200px; height: 3220px; overflow: hidden; }
  body {
    position: relative;
    background: var(--page);
    font-family: "Cabin", Arial, sans-serif;
    color: var(--ink);
  }
  .abs { position: absolute; }

  /* header */
  .top-rule { left: 0; top: 0; width: 1200px; height: 5px; background: var(--orange); }
  .nav-button {
    top: 79px; width: 260px; height: 63px;
    border: 3px solid var(--orange);
    color: var(--blue);
    font-family: "Dosis", Arial, sans-serif; font-weight: 500;
    font-size: 26px; letter-spacing: 0.5px;
    display: flex; align-items: center; justify-content: center;
  }
  .brand { left: 860px; top: 40px; width: 260px; height: 150px; }
  .brand-dot { position: absolute; right: 30px; top: 0; width: 70px; height: 70px; border-radius: 50%; background: var(--blue); }
  .brand-name {
    position: absolute; right: 0; top: 76px; text-align: right;
    font-family: "Cabin", Arial, sans-serif; font-weight: 400;
    font-size: 46px; line-height: 48px; color: var(--ink);
  }

  /* hero */
  .hero { left: 0; top: 221px; width: 1200px; height: 470px;
    background: linear-gradient(110deg, #22313c 0%, #3f6577 35%, #7fa2b2 60%, #2b3c47 100%); }
  .hero-line {
    left: 71px; background: rgba(12, 14, 18, 0.78);
    color: #f2f2f2; font-family: "Dosis", Arial, sans-serif; font-weight: 500;
    font-size: 62px; line-height: 81px; padding: 0 22px; letter-spacing: 1px;
  }
  .hero-sub { left: 102px; top: 525px; color: #e2e6e8; font-size: 23px; }
  .slide-dot { top: 652px; width: 14px; height: 14px; border-radius: 50%; background: #c9ccce; }
  .slide-dot.is-active { background: var(--blue); }
  .round-button { width: 128px; height: 128px; border-radius: 50%; background: var(--orange);
    display: flex; align-items: center; justify-content: center; }

  /* about */
  .section-title { font-family: "Dosis", Arial, sans-serif; font-weight: 500; }
  .about-title { left: 103px; top: 789px; font-size: 31px; color: var(--blue); }
  .about-text { left: 103px; top: 852px; width: 650px; font-size: 13.4px; line-height: 21px; color: #3a3a3a; }
  .team-figure { left: 830px; top: 812px; width: 285px; height: 176px;
    background: linear-gradient(90deg, #222 0%, #1e9fd8 30%, #222 50%, #1e9fd8 70%, #222 100%); border-radius: 6px; }

  /* form sections */
  .photo-band { left: 0; width: 1200px; }
  .hire-band { top: 1067px; height: 575px;
    background: linear-gradient(120deg, #38505c 0%, #6f8e9c 40%, #a9bfc7 60%, #3d5561 100%); }
  .work-band { top: 1846px; height: 576px;
    background: linear-gradient(120deg, #3a5866 0%, #7196a6 45%, #9ab5bf 65%, #2f4651 100%); }
  .section-label {
    color: #fff; font-family: "Dosis", Arial, sans-serif; font-weight: 500;
    font-size: 46px; display: flex; align-items: center; padding-left: 22px;
  }
  .label-blue { background: var(--blue); }
  .label-orange { background: var(--orange); }
  .label-dark { background: var(--label-dark); }
  .field {
    height: 49px; background: var(--field); color: var(--field-text);
    font-size: 18px; display: flex; align-items: center; padding-left: 22px; gap: 14px;
  }
  .field.is-message { align-items: flex-start; padding-top: 14px; }
  .field .caret { font-size: 15px; color: #e8e8e8; }
  .submit {
    width: 176px; height: 46px; color: #fff; font-family: "Dosis", Arial, sans-serif;
    font-weight: 600; font-size: 19px; display: flex; align-items: center; justify-content: center;
  }
  .submit-blue { background: var(--blue); }
  .submit-orange { background: var(--orange); }
  .email-note { left: 620px; top: 2259px; font-size: 18px; color: #d9dcde; }
  .email-note span { color: var(--orange); }

  /* browse rows */
  .browse { left: 0; width: 1200px; display: flex; align-items: center; justify-content: center; gap: 18px;
    font-family: "Dosis", Arial, sans-serif; font-weight: 500; font-size: 45px; letter-spacing: 0.5px; }
  .browse-talents { top: 1718px; height: 80px; color: var(--blue); }
  .browse-jobs { top: 2474px; height: 80px; color: var(--orange); }

  /* contact */
  .grey-band { left: 0; width: 1200px; background: var(--rule); }
  .map-area { left: 0; top: 2602px; width: 1200px; height: 354px;
    background: linear-gradient(135deg, #9fcde2 0%, #b7dcec 50%, #96c6dc 100%); }

  /* footer */
  .footer-brand { left: 101px; top: 3010px; display: flex; align-items: center; gap: 10px;
    font-size: 30px; color: var(--ink); }
  .footer-brand .dot { width: 26px; height: 26px; border-radius: 50%; background: var(--blue); }
  .info { font-size: 18px; line-height: 26px; }
  .info-label { color: var(--ink); }
  .info-value { color: var(--muted); }
  .copyright { left: 103px; top: 3167px; font-size: 9px; color: #8a8a8a; }
</style>
</head>
<body>

  <div class="abs top-rule"></div>

  <header>
    <a class="abs nav-button" style="left:101px">HIRE TALENT</a>
    <a class="abs nav-button" style="left:408px">FIND WORK</a>
    <div class="abs brand">
      <span class="brand-dot"></span>
      <span class="brand-name">Norvik<br>Staffing</span>
    </div>
  </header>

  <section class="hero-block">
    <div class="abs hero" role="img" aria-label="Photo of hands typing on a laptop keyboard in blue light"></div>
    <div class="abs hero-line" style="top:353px">15 YEARS OF EXCELLENCE</div>
    <div class="abs hero-line" style="top:434px">RECRUITMENT AND PASSION</div>
    <p class="abs hero-sub">We helped thousands of&nbsp; people to match with the perfect companies</p>
    <span class="abs slide-dot is-active" style="left:996px"></span>
    <span class="abs slide-dot" style="left:1030px"></span>
    <span class="abs slide-dot" style="left:1064px"></span>
    <span class="abs slide-dot" style="left:1098px"></span>
    <a class="abs round-button" style="left:550px;top:627px">
      <svg width="40" height="24" viewBox="0 0 40 24"><polyline points="4,4 20,19 36,4" fill="none" stroke="#fff" stroke-width="4"/></svg>
    </a>
  </section>

  <section class="about">
    <h2 class="abs section-title about-title">ABOUT US</h2>
    <p class="abs about-text">Lorem ipsum dolor sit amet, consectetuer adipiscing elit, sed diam nonummy nibh euismod tincidunt ut laoreet dolore magna aliquam erat volutpat. Ut wisi enim ad minim veniam, quis nostrud exerci tation ullamcorper suscipit lobortis nisl ut aliquip ex ea commodo consequat. Duis autem vel eum iriure dolor in hendrerit in vulputate velit esse molestie consequat, vel illum dolore eu feugiat nulla facilisis at vero eros et accumsan et iusto odio dignissim qui blandit praesent luptatum zzril delenit augue duis dolore te feugait nulla facilisi. Nam liber tempor cum soluta nobis eleifend option congue nihil imperdiet doming id quod mazim placerat facer assum. congue nihil imperdiet doming id quod mazim placerat facer assum.</p>
    <div class="abs team-figure" role="img" aria-label="Illustration of a group of five standing people in black and blue"></div>
  </section>

  <section class="hire-talent">
    <div class="abs photo-band hire-band" role="img" aria-label="Blurred photo of an office workplace"></div>
    <h2 class="abs section-label label-blue" style="left:77px;top:1103px;width:303px;height:84px">HIRE TALENT</h2>
    <div class="abs field" style="left:230px;top:1228px;width:354px">Company Name</div>
    <div class="abs field" style="left:616px;top:1228px;width:354px">Contact Name</div>
    <div class="abs field" style="left:230px;top:1297px;width:354px">Email</div>
    <div class="abs field" style="left:616px;top:1297px;width:354px">Phone</div>
    <div class="abs field" style="left:230px;top:1365px;width:354px">Address</div>
    <div class="abs field" style="left:616px;top:1365px;width:354px">What you are looking for <span class="caret">▼</span></div>
    <div class="abs field is-message" style="left:230px;top:1428px;width:740px;height:103px">Tell us how can we help you</div>
    <a class="abs submit submit-blue" style="left:513px;top:1554px">SUBMIT</a>
  </section>

  <svg class="abs" style="left:547px;top:1641px" width="100" height="56" viewBox="0 0 100 56"><polygon points="0,0 100,0 50,56" fill="#3f5560"/></svg>

  <a class="abs browse browse-talents">
    <svg width="82" height="82" viewBox="0 0 82 82"><circle cx="33" cy="33" r="25" fill="none" stroke="#1e9fd8" stroke-width="7"/><line x1="52" y1="52" x2="76" y2="76" stroke="#1e9fd8" stroke-width="9" stroke-linecap="round"/></svg>
    BROWSE TALENTS
  </a>

  <section class="find-work">
    <div class="abs photo-band work-band" role="img" aria-label="Blurred photo of an open-plan office with computers"></div>
    <h2 class="abs section-label label-orange" style="left:75px;top:1883px;width:275px;height:86px">FIND WORK</h2>
    <div class="abs field" style="left:230px;top:2037px;width:354px">Full Name</div>
    <div class="abs field" style="left:616px;top:2037px;width:354px">What is your profession <span class="caret">▼</span></div>
    <div class="abs field" style="left:230px;top:2106px;width:354px">Email</div>
    <div class="abs field" style="left:616px;top:2106px;width:354px">Phone</div>
    <div class="abs field" style="left:230px;top:2173px;width:354px">Address</div>
    <div class="abs field" style="left:616px;top:2173px;width:354px">What you are looking for <span class="caret">▼</span></div>
    <div class="abs field" style="left:230px;top:2241px;width:300px">Attached your resume here
      <svg width="20" height="26" viewBox="0 0 20 26"><path d="M1 1h12l6 6v18H1z" fill="#eee"/><path d="M13 1v6h6" fill="#bbb"/><line x1="5" y1="13" x2="15" y2="13" stroke="#555" stroke-width="1.5"/><line x1="5" y1="17" x2="15" y2="17" stroke="#555" stroke-width="1.5"/><line x1="5" y1="21" x2="15" y2="21" stroke="#555" stroke-width="1.5"/></svg>
    </div>
    <p class="abs email-note">Or email us at <span>careers@norvikstaffing.com</span></p>
    <a class="abs submit submit-orange" style="left:513px;top:2334px">SUBMIT</a>
  </section>

  <svg class="abs" style="left:560px;top:2421px" width="76" height="38" viewBox="0 0 76 38"><polygon points="0,0 76,0 38,38" fill="#5a7b88"/></svg>

  <a class="abs browse browse-jobs">
    <svg width="82" height="82" viewBox="0 0 82 82"><circle cx="33" cy="33" r="25" fill="none" stroke="#f15a22" stroke-width="7"/><line x1="52" y1="52" x2="76" y2="76" stroke="#f15a22" stroke-width="9" stroke-linecap="round"/></svg>
    BROWSE JOBS
  </a>

  <section class="contact">
    <div class="abs grey-band" style="top:2587px;height:15px"></div>
    <div class="abs map-area" role="img" aria-label="Street map of the city centre showing the office location"></div>
    <svg class="abs" style="left:502px;top:2733px" width="52" height="72" viewBox="0 0 52 72"><path d="M26 2C12 2 2 12 2 26c0 18 24 44 24 44s24-26 24-44C50 12 40 2 26 2z" fill="#1b1b1b"/><circle cx="26" cy="26" r="10" fill="#1e9fd8"/></svg>
    <h2 class="abs section-label label-dark" style="left:77px;top:2641px;width:288px;height:86px">CONTACT US</h2>
    <div class="abs grey-band" style="top:2956px;height:18px"></div>
  </section>

  <footer>
    <div class="abs footer-brand"><span class="dot"></span>Norvik Staffing</div>
    <div class="abs info info-label" style="left:410px;top:3026px">Address</div>
    <div class="abs info info-value" style="left:492px;top:3026px">123 - Level 1 Building XYZ<br>Name the Street City<br>Postcode 123456 Country Name</div>
    <div class="abs info info-label" style="left:816px;top:3026px">Phone</div>
    <div class="abs info info-value" style="left:897px;top:3026px">1234 567 890</div>
    <div class="abs info info-label" style="left:816px;top:3076px">Email</div>
    <div class="abs info info-value" style="left:897px;top:3076px">careers@norvikstaffing.com</div>
    <p class="abs copyright">©2015 Copyright Norvik Staffing</p>
    <a class="abs round-button" style="left:524px;top:3145px;width:150px;height:150px">
      <svg width="40" height="24" viewBox="0 0 40 24" style="margin-top:-60px"><polyline points="4,20 20,5 36,20" fill="none" stroke="#fff" stroke-width="4"/></svg>
    </a>
  </footer>

</body>
</html>
```